Business card design needed

We would like a new design for our window furnishings & home decor business. We supply & install blinds, curtains, shutters etc. We are about to incorporate home decor products like cushoins & throws...
We'd like to use moderns browns & green tones. Casual but elegant style. Maybe textured/patterned look design. Design should communicate quality and great value with latest designs.

website & FB page & email is still to be advised so pls provide space.

Industry/Entity Type

Business

Contact Information for Business Card

Marlowe Haven
Window Furnishings & Home Decor
Genevieve - Interior Stylist
Call us now for a free measure & quote - 63124089
0412 906 358
0418 273 564

```html
<!DOCTYPE html>
<html lang="en">
<head>
<meta charset="utf-8">
<title>Marlowe Haven – Business Card</title>
<link rel="stylesheet" href="https://fonts.googleapis.com/css2?family=Open+Sans:wght@400;600;700&display=swap">
<style>
  :root {
    --page-bg: #1c1c1c;
    --card-charcoal: #434343;
    --card-white: #ffffff;
    --brand-tan: #c3a88a;
    --text-white: #ffffff;
    --text-ink: #111111;
    --ribbon-green: #6a9a3c;
    --ribbon-green-soft: rgba(106, 154, 60, 0.18);
  }
  * { margin: 0; padding: 0; box-sizing: border-box; }
  html, body {
    width: 1200px;
    height: 900px;
    overflow: hidden;
    background: var(--page-bg);
    font-family: "Open Sans", Arial, sans-serif;
  }
  .canvas { position: relative; width: 1200px; height: 900px; }

  .card {
    position: absolute;
    width: 616px;
    height: 340px;
    border-radius: 18px;
    overflow: hidden;
  }
  .card--front { left: 113px; top: 100px; background: var(--card-charcoal); }
  .card--back  { left: 453px; top: 461px; background: var(--card-white); }

  .ribbon-pattern {
    position: absolute;
    background: linear-gradient(135deg, transparent 10%, var(--ribbon-green-soft) 45%, rgba(106,154,60,0.32) 60%, transparent 90%);
    border-radius: 40% 60% 50% 50%;
  }

  .brand { position: absolute; color: var(--brand-tan); white-space: nowrap; }
  .brand__mark {
    position: absolute;
    left: -48px; top: 4px;
    width: 38px; height: 38px;
    border-radius: 50%;
    background: var(--text-white);
  }
  .brand__name { font-size: 37px; font-weight: 400; line-height: 1; letter-spacing: -0.3px; }
  .brand__tagline { font-size: 13px; font-weight: 400; margin-top: 2px; margin-left: 2px; }

  .person { position: absolute; left: 63px; top: 180px; }
  .person__name { color: var(--text-white); font-size: 23px; font-weight: 700; line-height: 1.1; }
  .person__role { color: var(--brand-tan); font-size: 13.5px; margin-left: 60px; line-height: 1.1; }

  .contact { position: absolute; left: 123px; top: 256px; font-size: 12.5px; line-height: 17px; }
  .contact__lead { color: var(--text-white); }
  .contact__line { color: var(--brand-tan); display: flex; align-items: center; gap: 5px; }
  .contact__line svg { fill: var(--text-white); flex: none; }

  .back__panel { position: absolute; left: 0; top: 0; width: 174px; height: 100%; background: var(--card-charcoal); }
  .back__band  { position: absolute; left: 0; top: 38px; width: 100%; height: 109px; background: var(--card-charcoal); }

  .fields { position: absolute; left: 270px; top: 210px; font-size: 9.5px; color: var(--text-ink); }
  .field { display: flex; align-items: flex-end; height: 14.5px; }
  .field__label { width: 48px; }
  .field__rule { width: 166px; border-bottom: 1.2px solid var(--text-ink); margin-bottom: 2px; }
</style>
</head>
<body>
<main class="canvas">

  <section class="card card--front" aria-label="Business card front">
    <div class="ribbon-pattern" role="img" aria-label="Flowing green line ribbon pattern" style="left:22px; top:18px; width:140px; height:132px;"></div>
    <div class="ribbon-pattern" role="img" aria-label="Large flowing green line ribbon pattern" style="left:392px; top:10px; width:210px; height:300px;"></div>

    <div class="brand" style="left:102px; top:72px;">
      <span class="brand__mark"></span>
      <div class="brand__name">Marlowe Haven</div>
      <div class="brand__tagline">Window Furnishings &amp; Home Decor</div>
    </div>

    <div class="person">
      <div class="person__name">Genevieve</div>
      <div class="person__role">Interior Stylist</div>
    </div>

    <div class="contact">
      <div class="contact__lead">Call us now for a free measure &amp; quote:</div>
      <div class="contact__line">
        <svg width="10" height="10" viewBox="0 0 24 24" aria-hidden="true"><path d="M6.6 10.8a15.1 15.1 0 0 0 6.6 6.6l2.2-2.2a1 1 0 0 1 1-.25 11.4 11.4 0 0 0 3.6.57 1 1 0 0 1 1 1V20a1 1 0 0 1-1 1A17 17 0 0 1 3 4a1 1 0 0 1 1-1h3.5a1 1 0 0 1 1 1c0 1.25.2 2.45.57 3.57a1 1 0 0 1-.25 1z"/></svg>
        63124089
      </div>
      <div class="contact__line">
        <svg width="10" height="11" viewBox="0 0 14 20" aria-hidden="true"><path d="M3 0h8a2 2 0 0 1 2 2v16a2 2 0 0 1-2 2H3a2 2 0 0 1-2-2V2a2 2 0 0 1 2-2zm0 2.5v13h8v-13zM7 16.5a1 1 0 1 0 0 2 1 1 0 0 0 0-2z"/></svg>
        0412-906-358 or 0418-273-564
      </div>
    </div>
  </section>

  <section class="card card--back" aria-label="Business card back">
    <div class="back__panel"></div>
    <div class="back__band"></div>
    <div class="ribbon-pattern" role="img" aria-label="Flowing green line ribbon pattern" style="left:22px; top:18px; width:140px; height:132px;"></div>

    <div class="brand" style="left:102px; top:72px;">
      <span class="brand__mark"></span>
      <div class="brand__name" style="font-size:35px;">Marlowe Haven</div>
      <div class="brand__tagline" style="font-size:12.5px;">Window Furnishings &amp; Home Decor</div>
    </div>

    <div class="fields">
      <div class="field"><span class="field__label">Email:</span><span class="field__rule"></span></div>
      <div class="field"><span class="field__label">Web:</span><span class="field__rule"></span></div>
      <div class="field"><span class="field__label">FB page:</span><span class="field__rule"></span></div>
    </div>
  </section>

</main>
</body>
</html>
```